Bluebird Business Card Design

Name Marlene Obadofor
Title Mortgage Originator
Office (800) 416-2795 x65
Direct (240) 615-2079
Email mobadofor@bluebirdlending.example
NMLS 3817465
Licensed MD

Name Dorian Pelletier
Title Mortgage Originator
Office (800) 416-2795 x66
Direct (404) 263-5147
Email dpelletier@bluebirdlending.example
NMLS 3156702
Licensed MD

Name Rochelle Barnaby
Title Mortgage Originator
Office (800) 416-2795 x67
Direct (443) 812-3659
Email barnabyrochelle@mailpost.example
NMLS 3902576
Licensed MD

Name Omar Teldouri
Title Mortgage Originator
Office (800) 416-2795 x32
Direct (571) 326-7045
Email oteldouri@bluebirdlending.example
NMLS 1573064
Licensed MD

```html
<!DOCTYPE html>
<html lang="en">
<head>
<meta charset="utf-8">
<title>Bluebird Business Card</title>
<link href="https://fonts.googleapis.com/css2?family=Cormorant+Garamond:wght@500;600;700&family=Arimo:wght@400;500&display=swap" rel="stylesheet">
<style>
  :root {
    --navy-deep: #031447;
    --navy: #0a2a78;
    --royal: #1553a8;
    --gold: #d4a24c;
    --ink: #1a2340;
    --white: #ffffff;
    --stage: #e4e4e4;
  }
  * { margin: 0; padding: 0; box-sizing: border-box; }
  html, body { width: 1200px; height: 1200px; overflow: hidden; }
  body { background: var(--stage); position: relative; font-family: "Arimo", Arial, sans-serif; }

  .card { position: absolute; left: 181px; width: 837px; height: 477px; overflow: hidden; }

  .card-front {
    top: 91px;
    background: radial-gradient(ellipse 70% 80% at 25% 20%, var(--royal) 0%, var(--navy) 45%, var(--navy-deep) 100%);
    display: flex; align-items: center; justify-content: center;
  }
  .brand { display: flex; align-items: center; gap: 22px; color: var(--white);
    font-family: "Cormorant Garamond", Georgia, serif; font-weight: 700; white-space: nowrap; }
  .brand-mark { width: 54px; height: 54px; border-radius: 50%; background: var(--gold); flex: none; }
  .brand-front .brand-name { font-size: 64px; letter-spacing: 1px; line-height: 1; }

  .card-back { top: 631px; background: var(--white); }
  .photo {
    position: absolute; left: 0; top: 0; width: 367px; height: 477px;
    background: radial-gradient(ellipse 60% 70% at 55% 50%, #6b5142 0%, #3d3a44 50%, #2b3142 100%);
  }
  .card-curves { position: absolute; inset: 0; width: 837px; height: 477px; }

  .brand-back { position: absolute; left: 407px; width: 360px; top: 140px; justify-content: center; gap: 12px; color: var(--navy); }
  .brand-back .brand-mark { width: 28px; height: 28px; }
  .brand-back .brand-name { font-size: 29px; line-height: 1; }

  .person { position: absolute; left: 441px; top: 236px; }
  .person-name { font-family: "Cormorant Garamond", Georgia, serif; font-weight: 700; font-size: 38px; color: var(--navy-deep); line-height: 1; }
  .person-title { font-family: "Cormorant Garamond", Georgia, serif; font-weight: 500; font-size: 24px; color: var(--gold); margin-top: 8px; letter-spacing: .3px; }

  .contact { position: absolute; left: 440px; top: 346px; list-style: none; }
  .contact li { display: flex; align-items: center; gap: 12px; font-size: 20px; color: var(--ink); height: 31px; white-space: nowrap; }
  .contact svg { width: 26px; height: 22px; flex: none; fill: var(--gold); }
  .license { position: absolute; left: 478px; top: 441px; font-size: 17px; color: #3a4260; letter-spacing: .3px; }
</style>
</head>
<body>
  <section class="card card-front">
    <div class="brand brand-front">
      <span class="brand-mark"></span>
      <span class="brand-name">Bluebird Financial Services</span>
    </div>
  </section>

  <section class="card card-back">
    <div class="photo" role="img" aria-label="Portrait photo of the mortgage originator"></div>
    <svg class="card-curves" viewBox="0 0 837 477" aria-hidden="true">
      <defs>
        <linearGradient id="blueCorner" x1="0" y1="0" x2="1" y2="1">
          <stop offset="0" stop-color="#1553a8"/>
          <stop offset="1" stop-color="#031447"/>
        </linearGradient>
      </defs>
      <path d="M640 0 Q770 60 837 172 L837 0 Z" fill="url(#blueCorner)"/>
      <path d="M640 0 Q770 60 837 172" fill="none" stroke="var(--gold)" stroke-width="6"/>
      <path d="M0 290 Q40 410 200 477 L0 477 Z" fill="url(#blueCorner)"/>
      <path d="M0 290 Q40 410 200 477" fill="none" stroke="var(--gold)" stroke-width="5"/>
    </svg>

    <div class="brand brand-back">
      <span class="brand-mark"></span>
      <span class="brand-name">Bluebird Financial Services</span>
    </div>

    <div class="person">
      <h1 class="person-name">Marlene Obadofor</h1>
      <p class="person-title">Mortgage Originator</p>
    </div>

    <ul class="contact">
      <li><svg viewBox="0 0 24 24"><path d="M6.6 10.8a15.1 15.1 0 0 0 6.6 6.6l2.2-2.2c.3-.3.7-.4 1-.2 1.1.4 2.3.6 3.6.6.6 0 1 .4 1 1V20c0 .6-.4 1-1 1A17 17 0 0 1 3 4c0-.6.4-1 1-1h3.5c.6 0 1 .4 1 1 0 1.3.2 2.5.6 3.6.1.3 0 .7-.2 1z"/></svg>Office (800) 416-2795 x 65</li>
      <li><svg viewBox="0 0 24 24"><path d="M6.6 10.8a15.1 15.1 0 0 0 6.6 6.6l2.2-2.2c.3-.3.7-.4 1-.2 1.1.4 2.3.6 3.6.6.6 0 1 .4 1 1V20c0 .6-.4 1-1 1A17 17 0 0 1 3 4c0-.6.4-1 1-1h3.5c.6 0 1 .4 1 1 0 1.3.2 2.5.6 3.6.1.3 0 .7-.2 1z"/></svg>Direct (240) 615-2079</li>
      <li><svg viewBox="0 0 26 20"><path d="M1 2h24v16H1z M2.5 3.5 13 11 23.5 3.5" fill="none" stroke="var(--gold)" stroke-width="2"/></svg>mobadofor@bluebirdlending.example</li>
    </ul>
    <p class="license">NMLS 3817465 • Licensed MD</p>
  </section>
</body>
</html>
```